Flyer-Design für Hundeschule
Zielgruppe
Ich habe eine Hundeschule, seit 11 Jahren, die sich gerade neu aufstellt. Meine Zielgruppe sind junge bis mittel alte Hundemenschen die ihren Hund erziehen möchten und gerne auch ihr Freizeit mit ihm verbringen.
Aufgabenstellung
Ich möchte gerne ein Design was Neukunden anspricht.
Gerne auch, was man sich an den Kühlschrank hängt, weil es so schön ist ;-)
Ich habe sehr viele Fotos vom Profi und kann immer nachliefern, falls deiner Meinung nach etwas nicht ganz passt.
Das Logo habe ich in allen möglichen Dateiformen. Kann ich auch gerne nachliefern.
Vielleicht ist es auch zu viel Text?
Ich bin für alles offen :-)
Die Flyer möchte ich dann bei papier-flott-shop.de bestellen.
Ich freue mich auf deinen Vorschlag!

```html
<!DOCTYPE html>
<html lang="de">
<head>
<meta charset="utf-8">
<title>PfotenFreunde – Flyer Hundetraining</title>
<link href="https://fonts.googleapis.com/css2?family=Open+Sans:wght@400;600;700;800&family=Caveat:wght@700&display=swap" rel="stylesheet">
<style>
:root{
  --teal:#5fb3ae;
  --red:#c8392b;
  --ink:#333333;
  --brown:#5a3a2e;
  --paper:#f6f6f5;
  --bg:#e2e2e2;
  --photo-green:#8fa86a;
  --photo-grey:#cfc9c2;
  --photo-blue:#7fa3b5;
}
*{box-sizing:border-box;margin:0;padding:0}
html,body{width:1200px;height:1054px;overflow:hidden;background:var(--bg);font-family:"Open Sans",Arial,sans-serif;color:var(--ink)}
.spread{position:absolute;left:40px;width:1120px;height:500px;display:flex;box-shadow:0 6px 18px rgba(0,0,0,.12)}
.spread--outside{top:20px}
.spread--inside{top:534px}
.panel{position:relative;width:560px;height:100%;background:var(--paper);overflow:hidden}
.panel + .panel{border-left:1px solid #e2e2e0}

/* outside back */
.intro{position:absolute;top:52px;left:60px;right:60px;text-align:center;font-size:13px;line-height:1.55}
.intro p{margin-bottom:8px}
.chevron{color:var(--teal);font-weight:800;font-size:26px;letter-spacing:-6px;position:absolute}
.chevron--r{left:40px;top:205px}
.chevron--l{right:40px;top:40px}
.signature{font-family:"Caveat",cursive;color:var(--red);font-size:34px;position:absolute;top:238px;left:0;right:0;text-align:center}
.back-url{position:absolute;left:28px;right:20px;top:382px;font-weight:800;font-size:23px;line-height:1.2;color:var(--brown);white-space:nowrap}
.band{position:absolute;left:0;right:0;bottom:0;background:var(--teal)}
.band--back{height:72px;color:#fff;font-size:9px;line-height:1.7;padding:20px 28px 0;white-space:nowrap}

/* outside front */
.band--front{height:200px}
.logo{position:absolute;top:48px;right:44px;text-align:right}
.logo__mark{display:inline-block;width:18px;height:18px;border-radius:50%;background:var(--teal);margin-right:10px;vertical-align:middle}
.logo__name{font-weight:700;font-size:44px;color:var(--red);vertical-align:middle}
.logo__rule{height:3px;background:var(--red);margin:6px 0 8px 60px}
.tagline{font-weight:700;font-size:17px;color:var(--brown)}
.photo{position:absolute;border-radius:50%;border:5px solid #fff;box-shadow:0 3px 10px rgba(0,0,0,.2)}
.photo--bulldog{width:200px;height:200px;right:28px;top:150px;background:radial-gradient(circle at 40% 55%,#e9dfd3,var(--photo-grey))}
.photo--group{width:180px;height:180px;left:36px;top:230px;background:radial-gradient(circle at 50% 60%,#b0a88a,var(--photo-green))}
.photo--dog{width:150px;height:150px;left:238px;top:262px;background:radial-gradient(circle at 50% 55%,#8c7658,var(--photo-green))}

/* inside */
.strip{position:absolute;left:0;right:0;bottom:0;height:22px;background:var(--teal)}
.copy{position:absolute;font-size:10.5px;line-height:1.45}
.copy h3{color:var(--red);font-size:11px;font-weight:700;margin:6px 0 2px}
.copy ul{list-style:none}
.copy li{margin-bottom:3px}
.copy b{font-weight:700}
.copy .cta{font-weight:700;margin-top:6px}
.copy .cta a{color:var(--red);text-decoration:none}
.copy--left{left:34px;top:30px;right:30px}
.copy--left .indent{margin-left:200px}
.photo--aussie{width:190px;height:190px;left:30px;top:200px;background:radial-gradient(circle at 45% 50%,#b08563,var(--photo-blue))}
.copy--workshops{left:34px;top:400px;right:30px}
.copy--col1{left:30px;top:30px;width:245px}
.copy--col2{left:290px;top:30px;width:245px}
.inline-chev{color:var(--teal);font-weight:800;letter-spacing:-4px;margin-right:6px}
.credit{position:absolute;right:24px;bottom:34px;font-size:9px;color:#777}
</style>
</head>
<body>

<section class="spread spread--outside">
  <article class="panel panel--back">
    <span class="chevron chevron--l">&lsaquo;&lsaquo;</span>
    <div class="intro">
      <p>Mein Name ist Katrin Walter, geb. 1986 in Merseburg.<br>Meine Leben teile ich mit meinem Mann, unserer Tochter und unseren vier Hunden und vier Katzen im schönen Wiesental. Seit 2009 bin ich Hundetrainerin aus Leidenschaft.</p>
      <p>Ich setze alles daran, dass Mensch und Hund durch meine Hilfe (wieder) ein Team werden.</p>
      <p>Ich freue mich auf dich und deine Fellnase(n)!<br>Liebe Grüße und hab eine gute Zeit,</p>
    </div>
    <span class="chevron chevron--r">&rsaquo;&rsaquo;</span>
    <div class="signature">Katrin Walter</div>
    <div class="back-url">www.hundetraining-pfotenfreunde.de</div>
    <div class="band band--back">
      | Hundetraining PfotenFreunde (ehemals Hundeschule Berger) | Katrin Walter | Lindenweg 7 | 06199 Auendorf |<br>
      Mail: mail@hundetraining-pfotenfreunde.de | Telefon/WhatsApp: 0151 - 234 567 89
    </div>
  </article>

  <article class="panel panel--front">
    <div class="band band--front"></div>
    <div class="logo">
      <span class="logo__mark"></span><span class="logo__name">PfotenFreunde</span>
      <div class="logo__rule"></div>
      <div class="tagline">Hundetraining für jede Schnauze</div>
    </div>
    <div class="photo photo--group" role="img" aria-label="Foto: Familie trainiert mit einem Hund im Park"></div>
    <div class="photo photo--dog" role="img" aria-label="Foto: Hund mit Geschirr sitzt zwischen Pylonen"></div>
    <div class="photo photo--bulldog" role="img" aria-label="Foto: Bulldogge gibt einer Hand die Pfote"></div>
  </article>
</section>

<section class="spread spread--inside">
  <article class="panel panel--groups">
    <div class="copy copy--left">
      <h3>Exklusives Einzeltraining oder doch gemeinsam in einer Hundegruppe lernen?</h3>
      <p>Ich biete dir eine individuelle Lösung.</p>
      <h3>Training in der Gruppe:</h3>
      <p>Gemeinsam lernen macht Spaß und fördert das Sozialverhalten deines Hundes.<br>Alle Kurse finden in 06199 Auendorf OT Wiesental statt.</p>
      <ul class="indent">
        <li>• <b>Welpenkurs:</b> Wir legen gemeinsam den optimalen Grundstein für einen sozialen und ruhigen Hund. – Anmeldung bis zur 14. Lebenswoche, Einstieg jederzeit, Dauer 8 Wochen, Kursgebühr 120 € –</li>
        <li>• <b>Junghundkurs:</b> Zusammen wachsen und aus dem jungen Wilden einen tollen Begleiter machen. – Anmeldung ab dem 4.–10. Monat, Dauer 12 Wochen, Kursgebühr 180 € –</li>
        <li>• <b>Benimm dich! – Kurs</b> – die vier Säulen des guten Benehmens in Perfektion.<br>· Modul 1: Sicherer Rückruf · Modul 2: Entspanntes Gehen an der Leine<br>· Modul 3: Führen und Folgen · Modul 4: Sitz-Platz-Bleib in Perfektion<br>– ab dem 10. Lebensmonat, je Modul 60 €, alle Module 220 € –</li>
      </ul>
    </div>
    <div class="photo photo--aussie" role="img" aria-label="Foto: Australian Shepherd springt durchs Wasser"></div>
    <div class="copy copy--workshops">
      <p><b>Workshops:</b> Manchmal hat man nur dieses eine, ganz spezielle Thema mit seinem Hund. Und man möchte genau hieran trainieren. Dann sind meine Workshops genau das Richtige. Immer wieder gibt es neue Themen, wie zum Beispiel „Die andere Art der Leinenführung“ oder „Der perfekte Rückruf“.<br>Wir trainieren hier in kleinen Gruppen, um dein Ziel zu erreichen.</p>
    </div>
    <div class="strip"></div>
  </article>

  <article class="panel panel--private">
    <div class="copy copy--col1">
      <h3>Lust auf Abenteuer und Spaß? Verbringe Zeit mit deinem Hund in meinen Beschäftigungskursen:</h3>
      <ul>
        <li>• <b>Crossdogging:</b> Du und dein Hund stellen sich wöchentlich neuen spannenden Aufgaben.</li>
        <li>• <b>Rally Obedience:</b> Geschicklichkeit und Gehorsam gepaart mit jeder Menge Spaß.</li>
        <li>• <b>Longieren:</b> Distanz schafft Nähe! Du arbeitest mit deinem Hund über die Distanz am Longierkreis.</li>
      </ul>
      <p class="cta"><span class="inline-chev">&rsaquo;&rsaquo;</span>Sichere dir jetzt deinen Platz im Kurs oder Workshop unter: <a>www.hundetraining-pfotenfreunde.de</a></p>
      <h3>Exklusives Einzeltraining</h3>
      <p>Im Einzeltraining liegt mein ganzer Fokus nur bei dir und deinem Hund. Die Trainings finden je nach Art bei dir Zuhause oder in Wiesental statt.</p>
      <ul>
        <li>• <b>Problemhundtherapie:</b> Dein Hund kann nicht alleine bleiben oder zeigt Aggressionen? Zusammen suchen wir nach der Ursache des Verhaltens.</li>
      </ul>
    </div>
    <div class="copy copy--col2">
      <p>Wir arbeiten uns Schritt für Schritt aus dem Problemverhalten heraus, hin zu einer harmonischen Mensch-Hund-Beziehung. (Training vorrangig bei dir Zuhause)</p>
      <ul>
        <li>• <b>Grunderziehung für Hunde ab 6 Monaten:</b> Ich zeige dir, wie du deinen Hund zu einem perfekten Begleiter machen kannst. Egal ob aus dem Tierheim adoptiert oder schon länger bei dir – kleinen Problemen des Alltags begegnen wir gemeinsam. (Training vorrangig in Auendorf)</li>
        <li>• <b>Welpenerziehung:</b> Ich zeige dir, wie du eine gute Basis schaffst, in der sich dein Welpe sicher fühlen kann. All das wirst du im Training lernen. (Training vorrangig in Auendorf)</li>
      </ul>
      <p class="cta"><span class="inline-chev">&rsaquo;&rsaquo;</span>Buche jetzt dein exklusives Einzeltraining unter: <a>www.hundetraining-pfotenfreunde.de</a></p>
    </div>
    <div class="credit">© Fotografien: Hundefoto Nord (Lena Brandt)</div>
    <div class="strip"></div>
  </article>
</section>

</body>
</html>
```